Health and wellnes company needs business cards

We are a Health and wellness business just relocated to Spain. Here nobody knows our business so we would like to put some of our services on the card. Clean design with logo.

Contact Information for Business Card

Brightmeadow
Clara & Tobias Wennberg
Calle de los Almendros 17
Villaserena del Mar
Mobile: 0046 731 402768
info@brightmeadow-example.se

Font styles to use
Serif

Colors
85cae6
85acd3
b768aa

Requirements
Must have
• these Services somewhere on the card
• - Private or group yoga
• - Reconnective healing
• - Kitesurfing lessons
• - Massage
• LOgo somewhere
Nice to have
• Colours that go with the logo please

```html
<!DOCTYPE html>
<html lang="en">
<head>
<meta charset="utf-8">
<title>Brightmeadow – Business Cards</title>
<link rel="stylesheet" href="https://fonts.googleapis.com/css2?family=Merriweather:wght@400;700&display=swap">
<style>
  :root {
    --canvas-bg: #e9e9e7;
    --card-bg: #111213;
    --card-bg-edge: #1b1c1e;
    --teal: #74cbd6;
    --teal-soft: #9fdbe3;
    --white: #f2f2f2;
    --ring-faint: #23282b;
  }
  * { box-sizing: border-box; margin: 0; padding: 0; }
  html, body {
    width: 1200px; height: 886px; overflow: hidden;
    background: var(--canvas-bg);
  }
  body { position: relative; font-family: "Merriweather", Georgia, serif; }

  .card {
    position: absolute;
    width: 560px; height: 320px;
    background: linear-gradient(160deg, var(--card-bg-edge), var(--card-bg) 60%);
    border-radius: 4px;
    box-shadow: 0 10px 28px rgba(0,0,0,.25);
    overflow: hidden;
  }

  /* Services side */
  .card--services { left: 60px; top: 90px; text-align: center; color: var(--teal); }
  .services { padding-top: 46px; }
  .services__title { font-weight: 700; font-size: 19px; margin-bottom: 8px; }
  .services__line { font-size: 18px; line-height: 1.35; }
  .brand-lockup {
    position: absolute; left: 0; right: 0; top: 190px;
    display: flex; flex-direction: column; align-items: center; gap: 12px;
  }
  .brand-lockup__dot {
    width: 54px; height: 54px; border-radius: 50%;
    background: radial-gradient(circle at 40% 35%, var(--teal-soft), var(--teal));
  }
  .brand-name {
    font-weight: 400; font-size: 30px; letter-spacing: 2px;
    color: var(--teal); text-transform: uppercase;
  }

  /* Contact side */
  .card--contact { left: 580px; top: 470px; }
  .contact__ring {
    position: absolute; right: -40px; top: -40px;
    width: 290px; height: 290px; border-radius: 50%;
    border: 16px solid var(--ring-faint);
  }
  .contact {
    position: absolute; left: 40px; bottom: 30px;
    color: var(--white);
  }
  .contact .brand-name { font-size: 32px; margin-bottom: 14px; }
  .contact__names { color: var(--teal); font-weight: 700; font-size: 18px; margin-bottom: 10px; }
  .contact__line { font-size: 14px; line-height: 1.55; display: flex; align-items: center; gap: 8px; }
  .contact__line svg { width: 12px; height: 12px; fill: var(--teal); flex: none; }
  .contact__plain { padding-left: 20px; }
  .contact__domain { color: var(--teal); }
</style>
</head>
<body>

<section class="card card--services">
  <div class="services">
    <p class="services__title">Our Services:</p>
    <p class="services__line">Private or group yoga | Reconnective healing</p>
    <p class="services__line">Kitesurfing lessons | Massage</p>
  </div>
  <div class="brand-lockup">
    <span class="brand-lockup__dot" aria-hidden="true"></span>
    <span class="brand-name">Brightmeadow</span>
  </div>
</section>

<section class="card card--contact">
  <span class="contact__ring" aria-hidden="true"></span>
  <div class="contact">
    <p class="brand-name">Brightmeadow</p>
    <p class="contact__names">Clara &amp; Tobias Wennberg</p>
    <p class="contact__line contact__plain">Calle de los Almendros 17</p>
    <p class="contact__line contact__plain">Villaserena del Mar</p>
    <p class="contact__line">
      <svg viewBox="0 0 24 24" aria-hidden="true"><path d="M6.6 10.8a15.1 15.1 0 0 0 6.6 6.6l2.2-2.2a1 1 0 0 1 1-.25 11.4 11.4 0 0 0 3.6.57 1 1 0 0 1 1 1V20a1 1 0 0 1-1 1A17 17 0 0 1 3 4a1 1 0 0 1 1-1h3.5a1 1 0 0 1 1 1c0 1.25.2 2.45.57 3.57a1 1 0 0 1-.25 1z"/></svg>
      0046 731 402768
    </p>
    <p class="contact__line">
      <svg viewBox="0 0 24 24" aria-hidden="true"><path d="M2 5h20v14H2z M3 6l9 7 9-7" /></svg>
      info@brightmeadow-example.se
    </p>
    <p class="contact__line">
      <svg viewBox="0 0 24 24" aria-hidden="true"><circle cx="12" cy="12" r="10"/></svg>
      <span>www.<span class="contact__domain">brightmeadow-example.se</span></span>
    </p>
  </div>
</section>

</body>
</html>
```